Senior care homes needs brochure design

I need a brochure design for a senior care home business, the company is based in Long Beach but have care houses in Long Beach and Huntington Beach California. We provide assisted living, independent living care for senior in a residential home. The name of the company is Willowmere Haven Inc. I would like to see designs that will go well with the color of my Logo that I will be attaching, I will need to add photos or houses, rooms, backyards. also I am thinking in the middle of the inside the services that we provide. The final design should communicate a caring home where anyone can trust their loved ones to us. I would like to incorporate the last picture of my grandpa if possible in a small picture. Under the Dorrance Map I want Facility # 418207359 and under Talbot Map I want Facility #

Target Market(s)

Baby boomers and older adults

Industry/Entity Type

Residential

Requirements
Must have
• must be able to add pictures and move content around

```html
<!DOCTYPE html>
<html lang="en">
<head>
<meta charset="utf-8">
<title>Willowmere Haven – Trifold Brochure</title>
<link href="https://fonts.googleapis.com/css2?family=Tinos:wght@400;700&display=swap" rel="stylesheet">
<style>
  :root{
    --teal:#1f8f93;
    --teal-dark:#137479;
    --aqua-light:#dcf0f0;
    --aqua-mid:#9fd6d6;
    --yellow:#f4c74c;
    --yellow-deep:#e9a92b;
    --ink:#3f4447;
    --white:#ffffff;
  }
  *{margin:0;padding:0;box-sizing:border-box}
  html,body{width:1200px;height:894px;overflow:hidden;background:#fff}
  body{font-family:"Tinos","Times New Roman",serif;color:var(--ink)}
  .brochure{position:relative;width:1200px;height:894px;overflow:hidden;background:var(--white)}
  .panel{position:absolute;top:0;height:894px}
  .panel--left{left:0;width:399px;background:var(--white)}
  .panel--center{left:399px;width:400px;background:var(--aqua-light)}
  .panel--right{left:799px;width:401px;background:var(--white)}

  .photo{position:absolute}
  .photo--bedroom{left:0;top:0;width:399px;height:267px;background:linear-gradient(180deg,#e6dfd2 0%,#c8b79f 55%,#8e6b5a 100%)}
  .photo--kitchen{left:0;top:0;width:401px;height:267px;background:linear-gradient(180deg,#f2efe9 0%,#b8b0a6 55%,#6d5a4c 100%)}
  .accent-stripe{position:absolute;left:0;top:267px;width:100%;height:11px;background:var(--yellow)}

  .intro{position:absolute;left:30px;top:296px;width:340px;font-size:14.6px;line-height:24.4px;text-align:justify}
  .mission{position:absolute;left:30px;top:578px;width:360px;font-size:20px;line-height:26px;font-weight:700;color:var(--teal)}
  .photo--hands{left:188px;top:654px;width:180px;height:122px;background:linear-gradient(135deg,#caa27c 0%,#8a5f3f 60%,#5b3a24 100%)}

  .brand{position:absolute;left:0;top:34px;width:400px;text-align:center}
  .brand__mark{display:block;width:50px;height:50px;margin:0 auto 42px;border-radius:50%;background:var(--teal)}
  .brand__name{font-size:27px;line-height:28px;letter-spacing:1px;font-variant:small-caps;color:var(--teal-dark);font-weight:400}
  .brand__tag{font-size:11px;letter-spacing:3.5px;color:var(--teal);margin-top:4px}

  .services-band{position:absolute;left:0;top:0;width:400px;height:894px}
  .section-title{position:absolute;left:0;width:400px;text-align:center;color:var(--yellow);font-weight:700;font-size:26px;line-height:30px}
  .section-title--standard{top:202px}
  .section-title--extra{top:638px}
  .service-list{position:absolute;list-style:none;color:var(--white);font-weight:700;font-size:14px;line-height:23.6px}
  .service-list li{padding-left:14px;text-indent:-12px}
  .service-list li::before{content:"•";display:inline-block;width:12px;text-indent:0}
  .service-list--standard{left:16px;top:271px;width:372px}
  .service-list--extra{left:22px;top:675px;width:370px}

  .photo--portrait{left:136px;top:282px;width:130px;height:196px;background:linear-gradient(180deg,#d8c7a3 0%,#b58f6d 50%,#6f6a58 100%);border:4px solid var(--white);box-shadow:0 0 0 1px #d7dede}
  .tagline-band{position:absolute;left:0;top:483px;width:401px;height:66px;background:var(--teal);color:var(--white);text-align:center;font-weight:700;font-size:19.5px;line-height:24px;padding-top:9px}
  .photo--residents{left:0;top:558px;width:401px;height:254px;background:linear-gradient(160deg,#cfd7c8 0%,#c9a678 45%,#86a3b9 100%)}

  .footer-bands{position:absolute;left:0;top:815px;width:1200px;height:79px}
  .footer-band{display:block;width:100%}
  .footer-band--aqua{height:16px;background:var(--aqua-mid)}
  .footer-band--yellow-line{height:7px;background:var(--yellow)}
  .footer-band--teal{height:28px;background:var(--teal)}
  .footer-band--yellow{height:14px;background:var(--yellow)}
  .footer-band--yellow-deep{height:14px;background:var(--yellow-deep)}
</style>
</head>
<body>
<div class="brochure">

  <section class="panel panel--left">
    <div class="photo photo--bedroom" role="img" aria-label="Photo of a bright shared bedroom with two twin beds and a dresser"></div>
    <div class="accent-stripe"></div>
    <p class="intro">At Willowmere Haven we know how important it is to place your loved ones in a safe, secure, comfortable and caring home. We believe that peace of mind and quality care should come standard. Our highly-trained and compassionate care givers are available 24/7 to assist with a variety of needs. We offer assistance with self-care tasks, medication management, activity programs, nutritious and well-balanced meal and snacks and daily laundry cleaning services. We stand for what we believe in and everything we do starts and ends with our Mission Statement:</p>
    <p class="mission">‘…to create a home that fosters<br>&nbsp;wellness, independence, dignity<br>&nbsp;and quality of life for each resident.’</p>
    <div class="photo photo--hands" role="img" aria-label="Photo of a caregiver's hands resting on a senior's hands holding a cane"></div>
  </section>

  <section class="panel panel--center">
    <svg class="services-band" viewBox="0 0 400 894" aria-hidden="true">
      <path d="M0 192 Q200 156 400 186 L400 894 L0 894 Z" fill="var(--teal)"/>
    </svg>
    <div class="brand">
      <span class="brand__mark"></span>
      <div class="brand__name">Willowmere Haven</div>
      <div class="brand__tag">Six Bed Senior Homes</div>
    </div>
    <h2 class="section-title section-title--standard">Standard<br>Services &amp; Amenities:</h2>
    <ul class="service-list service-list--standard">
      <li>24/7 trained, caring &amp; experienced staff.</li>
      <li>Medication management</li>
      <li>Activities programs</li>
      <li>Outdoor patio area for residents &amp; visitors,</li>
      <li>Assistance with self-care tasks (i.e. bathing,<br>grooming &amp; dressing)</li>
      <li>Private &amp; shared room options</li>
      <li>Clean and comfortable rooms</li>
      <li>Incontinence care</li>
      <li>Quiet, safe and well-established neighborhood.</li>
      <li>Wheel chair accessible rooms &amp; bath</li>
      <li>Daily cleaning/disinfecting and laundry services</li>
      <li>Nutritious and well-balanced home cooked meals<br>and snacks (special dietary needs can also be<br>accommodated).</li>
    </ul>
    <h2 class="section-title section-title--extra">Additional Services</h2>
    <ul class="service-list service-list--extra">
      <li>Visiting Health Care Professionals</li>
      <li>Transportation and Doctors Appointment escort.</li>
      <li>Mobile beautician services</li>
      <li>Respite care</li>
    </ul>
  </section>

  <section class="panel panel--right">
    <div class="photo photo--kitchen" role="img" aria-label="Photo of a modern kitchen with a round dining table and flowers"></div>
    <div class="accent-stripe"></div>
    <div class="photo photo--portrait" role="img" aria-label="Small portrait photo of a smiling senior man in a hat"></div>
    <div class="tagline-band">Experience the difference<br>of Willowmere Haven.</div>
    <div class="photo photo--residents" role="img" aria-label="Photo of seniors playing a table game together"></div>
  </section>

  <div class="footer-bands" aria-hidden="true">
    <span class="footer-band footer-band--aqua"></span>
    <span class="footer-band footer-band--yellow-line"></span>
    <span class="footer-band footer-band--teal"></span>
    <span class="footer-band footer-band--yellow"></span>
    <span class="footer-band footer-band--yellow-deep"></span>
  </div>

</div>
</body>
</html>
```